Business Card Design

The business card is for an IT services company with a specialism
in Integration Services Markets are Health, Government and finance, we provide Velmora SOA platforms and CWR Trellis integration. We are developing multi-agency connectivity

Industry/Entity Type

Business

Contact Information for Business Card

Martin Gorse
Director

BQVo Ltd Martin.gorse@bqvoltd.co.uk

Mobile: +44 (0) 7700900418
Tel: +44 (0) 1632 960583
Website: www.bqvoltd.co.uk

Fenwright House, Fenwright Square, Hollinbrook ZX98 4QT

Percival Hanley
Health Integration Services

Mobile +44 (0) 07700900276
Tel +44 (0) 1632 960583
Address as above

```html
<!DOCTYPE html>
<html lang="en">
<head>
<meta charset="utf-8">
<title>BQVo Ltd – Business Card</title>
<link href="https://fonts.googleapis.com/css2?family=Lato:wght@400;700&display=swap" rel="stylesheet">
<style>
  :root {
    --stage: #d9d9db;
    --card: #ffffff;
    --brand-blue: #2e3f9e;
    --name-blue: #3a4ba8;
    --text-grey: #8a8a8f;
    --rule-grey: #a9a9ae;
    --art-deep: #1c5fc4;
    --art-mid: #6fb2ea;
    --art-pale: #e6f2fc;
  }
  * { box-sizing: border-box; margin: 0; padding: 0; }
  html, body {
    width: 1200px;
    height: 900px;
    overflow: hidden;
    background: var(--stage);
    font-family: "Lato", "Helvetica Neue", Arial, sans-serif;
  }
  .business-card {
    position: absolute;
    left: 120px;
    top: 160px;
    width: 960px;
    height: 580px;
    background: var(--card);
    overflow: hidden;
  }
  .card-artwork {
    position: absolute;
    left: 0;
    top: 0;
    width: 470px;
    height: 100%;
    background:
      radial-gradient(ellipse 260px 160px at 60px 500px, var(--art-deep) 0%, rgba(28,95,196,0.55) 35%, rgba(111,178,234,0) 75%),
      radial-gradient(ellipse 200px 420px at 60px 160px, rgba(111,178,234,0.7) 0%, rgba(111,178,234,0) 70%),
      linear-gradient(90deg, var(--art-pale) 0%, rgba(230,242,252,0.6) 55%, rgba(255,255,255,0) 100%);
  }
  .card-details {
    position: absolute;
    left: 560px;
    top: 42px;
    width: 360px;
  }
  .company-name {
    font-weight: 700;
    font-size: 84px;
    line-height: 1;
    letter-spacing: 2px;
    color: var(--brand-blue);
  }
  .person-name {
    margin-top: 38px;
    font-size: 28px;
    font-weight: 400;
    letter-spacing: 1px;
    color: var(--name-blue);
    text-transform: uppercase;
    line-height: 1;
  }
  .person-role {
    font-size: 13px;
    letter-spacing: 1px;
    color: var(--text-grey);
    text-transform: uppercase;
    margin-top: 4px;
  }
  .dotted-rule {
    border: 0;
    border-top: 2px dotted var(--rule-grey);
    margin: 6px 0 10px;
  }
  .contact-list { list-style: none; }
  .contact-item {
    display: flex;
    align-items: center;
    height: 30px;
    font-size: 20px;
    color: var(--text-grey);
  }
  .contact-icon {
    width: 24px;
    height: 22px;
    margin-right: 14px;
    flex: none;
  }
  .contact-icon path, .contact-icon rect, .contact-icon circle, .contact-icon ellipse, .contact-icon line {
    fill: none;
    stroke: var(--brand-blue);
    stroke-width: 1.6;
  }
  .contact-icon .solid { fill: var(--brand-blue); stroke: none; }
  .address {
    font-size: 20px;
    font-style: normal;
    line-height: 1.6;
    color: var(--text-grey);
    margin-top: 4px;
  }
</style>
</head>
<body>
  <div class="business-card">
    <div class="card-artwork" role="img" aria-label="Abstract blue network of flowing fibres and scattered nodes radiating from the lower left"></div>

    <div class="card-details">
      <h1 class="company-name">BQVo</h1>

      <h2 class="person-name">Martin Gorse</h2>
      <p class="person-role">Director BQVo Ltd</p>
      <hr class="dotted-rule">

      <ul class="contact-list">
        <li class="contact-item">
          <svg class="contact-icon" viewBox="0 0 24 22" aria-hidden="true">
            <rect x="7" y="1" width="10" height="20" rx="1.5"/>
            <rect class="solid" x="9" y="4" width="6" height="7"/>
            <circle class="solid" cx="12" cy="17" r="1.4"/>
          </svg>
          <span>: +44 (0) 7700900418</span>
        </li>
        <li class="contact-item">
          <svg class="contact-icon" viewBox="0 0 24 22" aria-hidden="true">
            <path class="solid" d="M2 8 Q12 1 22 8 L19 11 L16 8 L8 8 L5 11 Z"/>
            <rect class="solid" x="5" y="11" width="14" height="9" rx="1.5"/>
          </svg>
          <span>: +44 (0) 1632 960583</span>
        </li>
        <li class="contact-item">
          <svg class="contact-icon" viewBox="0 0 24 22" aria-hidden="true">
            <rect x="2" y="4" width="20" height="14"/>
            <path d="M2 4 L12 12 L22 4"/>
          </svg>
          <span>: Martin.gorse@bqvoltd.co.uk</span>
        </li>
        <li class="contact-item">
          <svg class="contact-icon" viewBox="0 0 24 22" aria-hidden="true">
            <circle cx="12" cy="11" r="9"/>
            <ellipse cx="12" cy="11" rx="4" ry="9"/>
            <line x1="3" y1="11" x2="21" y2="11"/>
            <line x1="12" y1="2" x2="12" y2="20"/>
          </svg>
          <span>: www.bqvoltd.co.uk</span>
        </li>
      </ul>
      <hr class="dotted-rule">

      <address class="address">
        Fenwright House, Fenwright Square,<br>
        Hollinbrook ZX98 4QT
      </address>
    </div>
  </div>
</body>
</html>
```